MEDITERRANEAN Cafe Website needed

We are a MEDITERRANEAN Café serving Coffee, breakfast, Pizza, Pasta, Sandwiches etc.

We need a home page, menu & venue, Reservations & Events, Delivery
Connect (Social media / Feedback / Contact us),Join our team
Updates

Can we keep the designs in Mediterranean colours, look, and feel pleasethanks Added Saturday, December 10, 2016

Project Deadline Extended Reason: I have guarantied the payment and upgraded the project. I would like this would to give more time for new designs to come in and a couple of potential designs to show more. Added Sunday, December 11, 2016

Industry/Entity Type

Cafe

Coding

Coded - Design and coding required

Number of Pages Required

5+ page

Requirements
Must have
• MEDITERRANEAN feel, colours, style etc.
• http://www.quillandfen (DOT) co (DOT) uk
Nice to have

```html
<!DOCTYPE html>
<html lang="en">
<head>
<meta charset="utf-8">
<title>Lumera Café</title>
<link rel="stylesheet" href="https://fonts.googleapis.com/css2?family=Open+Sans:wght@400;600;700&family=Source+Sans+3:wght@300;400;600;700&display=swap">
<style>
:root{
  --maroon:#3d0b0e;
  --maroon-deep:#2a0608;
  --maroon-soft:#5a1216;
  --red:#d9100f;
  --orange:#f4a000;
  --gold:#dcae1c;
  --bronze:#a57806;
  --cream:#fdf5cc;
  --cream-card:#fffbe6;
  --ink:#1f1a17;
  --white:#ffffff;
}
*{margin:0;padding:0;box-sizing:border-box}
html,body{width:1200px;height:5056px;overflow:hidden}
body{position:relative;background:var(--maroon);font-family:"Open Sans",Arial,sans-serif;color:var(--ink)}
.abs{position:absolute}
.section{position:absolute;left:0;width:1200px}
.heading{font-family:"Source Sans 3","Open Sans",sans-serif;font-weight:400;text-align:center}
.center-x{left:0;width:100%;text-align:center}

/* header */
.hero{top:0;height:1028px;background:linear-gradient(180deg,#5c1014 0%,#470c10 55%,#3a090c 100%)}
.search{left:74px;top:34px;width:270px;height:33px;border:2px solid var(--orange);border-radius:6px;color:var(--white);font-size:13px;font-weight:600;padding:7px 12px}
.search svg{position:absolute;right:10px;top:6px}
.top-btn{top:34px;height:33px;border:2px solid var(--orange);border-radius:6px;color:var(--white);font-size:13px;font-weight:600;text-align:center;line-height:29px}
.brand{top:160px;left:0;width:1200px;display:flex;justify-content:center;align-items:center;gap:18px}
.brand-dot{width:38px;height:38px;border-radius:50%;background:var(--red)}
.brand-name{font-family:"Source Sans 3",sans-serif;font-weight:700;font-size:72px;color:var(--white);line-height:1}
.hero-dish{left:320px;top:330px;width:560px;height:520px;border-radius:50%;background:radial-gradient(circle at 45% 40%,#f2b13a 0%,#d46a1c 55%,#9b4a14 80%,#6b3010 100%)}
.arrow{width:30px;height:44px}
.dots{top:838px;left:530px;display:flex;gap:14px}
.dots span{width:14px;height:14px;border-radius:50%;background:#111}
.dots span:first-child{background:var(--orange)}

/* nav */
.nav{left:135px;top:883px;width:930px;height:145px;background:var(--red)}
.nav-link{top:108px;font-size:15px;color:var(--white);font-weight:600}
.nav-link.active{color:var(--orange)}

/* pasta band */
.pasta-band{top:1028px;height:489px;background:var(--cream)}
.pasta{left:337px;top:20px;width:472px;height:385px;border-radius:40% 45% 35% 40%;background:radial-gradient(ellipse at 50% 55%,#f7d66a 0%,#e7b63a 60%,#cf9a24 85%,rgba(253,245,204,0) 100%)}

/* story + menus */
.dark-band{top:1517px;height:1034px;background:linear-gradient(180deg,#3b0a0d,#2e0709)}
.menu-photo{left:100px;top:343px;width:945px;height:668px;border-radius:30px;background:linear-gradient(160deg,#6a3a28 0%,#4a2419 50%,#2f140e 100%);opacity:.85}
.story-card{left:135px;top:0;width:930px;height:337px;background:var(--white)}
.story-card h2{top:28px;font-size:72px;line-height:1;color:var(--ink)}
.story-card p{left:50px;width:830px;font-size:12.5px;line-height:20px;text-align:center;color:#333}
.read-more{font-size:13px;color:var(--orange);font-weight:600}
.menu-card{top:596px;height:374px;border:1.5px solid rgba(255,255,255,.8)}
.menu-badge{width:168px;height:168px;border-radius:50%;top:494px;color:var(--white);font-weight:700;font-size:21px;text-align:center;line-height:168px;font-family:"Source Sans 3",sans-serif}
.menu-badge svg{position:absolute;left:71px;top:30px}
.badge-breakfast{background:var(--orange)}
.badge-lunch{background:var(--gold)}
.badge-main{background:var(--bronze)}
.menu-from{top:745px;width:370px;text-align:center;color:var(--white);font-weight:700;font-size:22px}
.menu-price{top:783px;width:370px;text-align:center;color:var(--white);font-weight:700;font-size:40px;line-height:1}
.menu-price small{font-size:24px;font-weight:600}
.menu-taste{top:745px;width:297px;text-align:center;color:var(--white);font-weight:700;font-size:22px;line-height:46px}
.menu-link{top:930px;width:370px;text-align:center;color:var(--orange);font-size:13px}

/* team */
.team{top:2551px;height:792px;background:var(--cream)}
.team h2{top:130px;font-size:72px;line-height:1}
.team p{left:135px;width:930px;font-size:12.5px;line-height:21px;text-align:center;color:#333}
.portrait{top:438px;width:210px;height:210px;border-radius:50%;border:5px solid var(--white);box-shadow:0 0 0 1px #d9cfa8;background:radial-gradient(circle at 50% 40%,#d9c3ad 0%,#a9b6c4 60%,#e9eef2 100%)}
.member{top:686px;width:300px;text-align:center;color:var(--red);font-weight:700;font-size:15px}

/* reservation */
.reserve{top:3343px;height:482px;background:var(--maroon-deep)}
.reserve h2{top:55px;font-size:64px;color:var(--white);font-weight:400;line-height:1}
.reserve h3{top:140px;font-size:32px;color:var(--orange);font-weight:300;letter-spacing:1px}
.field{width:253px;height:44px;border:2px solid #cfc6c6;border-radius:6px;color:var(--white);font-size:13px;padding:11px 12px}
.btn{background:var(--orange);color:var(--white);font-size:13px;font-weight:600;text-align:center;border-radius:6px}

/* events */
.events-head{left:135px;top:3825px;width:930px;height:152px;background:var(--red)}
.events-head h2{top:8px;font-size:64px;color:var(--orange);font-weight:400;line-height:1.1}
.events-head h3{top:96px;font-size:28px;color:var(--orange);font-weight:300}
.events-head svg{position:absolute;top:26px}
.events{top:3977px;height:640px;background:var(--cream)}
.burger{left:152px;top:16px;width:455px;height:422px;border-radius:48% 48% 42% 42%;background:linear-gradient(180deg,#d08a3e 0%,#c9512c 35%,#6ba03a 55%,#8b4a2a 72%,#d99a4a 100%)}
.point{left:650px;width:400px;font-size:15px;line-height:22px;color:#333}
.point::before{content:"";position:absolute;left:0;top:6px;width:16px;height:16px;border-radius:50%;background:var(--red)}
.point span{display:block;padding-left:24px}
.events-caption{left:162px;top:472px;width:540px;font-size:12.5px;line-height:19px;color:#333}

/* footer */
.footer{top:4617px;height:388px;background:var(--cream)}
.footer h4{font-family:"Source Sans 3",sans-serif;font-weight:700;font-size:32px;color:var(--ink)}
.footer p{font-size:12.5px;line-height:20px;color:#333}
.social-dot{width:30px;height:30px;border-radius:50%;background:var(--ink)}
.contact-field{left:768px;width:267px;height:45px;border:1.5px solid #333;background:var(--white);font-size:13px;padding:12px 10px;color:#333}
.bottom-bar{top:5005px;height:51px;background:#2a0406;color:#d8c9c9;font-size:12px;text-align:center;line-height:51px;letter-spacing:.5px}
</style>
</head>
<body>

<header class="section hero">
  <div class="abs search">SEARCH FOOD
    <svg width="20" height="20" viewBox="0 0 20 20"><circle cx="8" cy="8" r="6" fill="none" stroke="#f4a000" stroke-width="2"/><line x1="12.5" y1="12.5" x2="18" y2="18" stroke="#f4a000" stroke-width="2.5"/></svg>
  </div>
  <div class="abs top-btn" style="left:883px;width:112px">JOIN NOW</div>
  <div class="abs top-btn" style="left:1004px;width:128px">RESERVATIONS</div>

  <div class="abs brand"><span class="brand-dot"></span><span class="brand-name">Lumera</span></div>

  <div class="abs hero-dish" role="img" aria-label="Pizza with a slice lifted on a wooden board"></div>

  <svg class="abs arrow" style="left:26px;top:558px" viewBox="0 0 30 44"><polyline points="24,4 6,22 24,40" fill="none" stroke="#f4a000" stroke-width="6"/></svg>
  <svg class="abs arrow" style="left:1144px;top:558px" viewBox="0 0 30 44"><polyline points="6,4 24,22 6,40" fill="none" stroke="#f4a000" stroke-width="6"/></svg>

  <div class="abs dots"><span></span><span></span><span></span><span></span><span></span></div>

  <nav class="abs nav">
    <svg class="abs" style="left:0;top:0" width="930" height="100" viewBox="0 0 930 100">
      <g stroke="#f4a000" stroke-width="3" fill="none">
        <line x1="269" y1="47" x2="357" y2="47"/>
        <line x1="419" y1="47" x2="509" y2="47"/>
        <line x1="571" y1="47" x2="661" y2="47"/>
        <circle cx="239" cy="47" r="30"/>
        <circle cx="388" cy="47" r="30"/>
        <circle cx="540" cy="47" r="30"/>
        <circle cx="691" cy="47" r="30"/>
      </g>
    </svg>
    <span class="abs nav-link active" style="left:98px">Home</span>
    <span class="abs nav-link" style="left:186px">About US</span>
    <span class="abs nav-link" style="left:302px">Our Story</span>
    <span class="abs nav-link" style="left:433px">Our Team</span>
    <span class="abs nav-link" style="left:556px">Menu</span>
    <span class="abs nav-link" style="left:653px">Events</span>
    <span class="abs nav-link" style="left:758px">Contact us</span>
  </nav>
</header>

<section class="section pasta-band">
  <div class="abs pasta" role="img" aria-label="Nests of tagliatelle pasta with a sprig of parsley"></div>
</section>

<section class="section dark-band">
  <div class="abs menu-photo" role="img" aria-label="Warm photo of baked pastries on a dark table"></div>

  <article class="abs story-card">
    <h2 class="abs heading center-x">Our Story</h2>
    <p class="abs" style="top:130px">An early morning walk to the bakery around the corner is a way of life in the Mediterranean. Nothing beats the first batch of bread from the oven to start your day. Lumera Café started with a simple idea: we wanted people to experience that taste all the time. So we combined a variety of best ingredients and delicacies to make you that healthy stuffed pita or fresh pizza to enjoy the way you like and whenever you get the urge to do so. As time went by we opened our hearts and ears to our customers and added a range of fresh and delicious products to our menu – salads, traditional Mediterranean starters, desserts and we made sure you don't miss out on the great morning lattes.</p>
    <span class="abs read-more center-x" style="top:283px">Read More</span>
  </article>

  <div class="abs menu-card" style="left:135px;width:370px"></div>
  <div class="abs menu-card" style="left:452px;width:370px"></div>
  <div class="abs menu-card" style="left:768px;width:297px"></div>

  <div class="abs menu-badge badge-breakfast" style="left:202px"><svg width="26" height="22" viewBox="0 0 26 22"><ellipse cx="8" cy="12" rx="5" ry="9" fill="#2a0608"/><ellipse cx="18" cy="14" rx="5" ry="7" fill="#2a0608"/></svg>BREAKFAST</div>
  <div class="abs menu-badge badge-lunch" style="left:519px"><svg width="26" height="22" viewBox="0 0 26 22"><ellipse cx="8" cy="12" rx="5" ry="9" fill="#2a0608"/><ellipse cx="18" cy="14" rx="5" ry="7" fill="#2a0608"/></svg>LUNCH</div>
  <div class="abs menu-badge badge-main" style="left:833px"><svg width="26" height="22" viewBox="0 0 26 22"><ellipse cx="8" cy="12" rx="5" ry="9" fill="#2a0608"/><ellipse cx="18" cy="14" rx="5" ry="7" fill="#2a0608"/></svg>MAIN MENU</div>

  <div class="abs menu-from" style="left:135px">FROM</div>
  <div class="abs menu-price" style="left:135px"><small>£</small>4.75</div>
  <div class="abs menu-from" style="left:452px">FROM</div>
  <div class="abs menu-price" style="left:452px"><small>£</small>6.95</div>
  <div class="abs menu-taste" style="left:768px">ENJOY THE TASTE<br>OF ITALY</div>

  <span class="abs menu-link" style="left:135px">View Menu</span>
  <span class="abs menu-link" style="left:452px">View Menu</span>
  <span class="abs menu-link" style="left:768px;width:297px">View Menu</span>
</section>

<section class="section team">
  <h2 class="abs heading center-x">Our Team</h2>
  <p class="abs" style="top:246px">One of the centerpieces and the Mediterranean symbol of Lumera Café are its colors which inspire a carefree wave, and invitation to relax in that particular world of Lumera Café. The mixture of captivating marina view and fresh ingredients is played in perfect harmony with the restaurant's atmosphere.</p>
  <p class="abs" style="top:296px">Our team has a great sense of pride in everything we do and a passion to ensure you have an incredible experience every time.</p>
  <span class="abs read-more center-x" style="top:338px">Read More</span>

  <svg class="abs arrow" style="left:26px;top:521px" viewBox="0 0 30 44"><polyline points="24,4 6,22 24,40" fill="none" stroke="#f4a000" stroke-width="6"/></svg>
  <svg class="abs arrow" style="left:1144px;top:521px" viewBox="0 0 30 44"><polyline points="6,4 24,22 6,40" fill="none" stroke="#f4a000" stroke-width="6"/></svg>

  <div class="abs portrait" style="left:138px" role="img" aria-label="Portrait photo of team member Dario Menzel"></div>
  <div class="abs portrait" style="left:495px" role="img" aria-label="Portrait photo of team member Paolo Reyes"></div>
  <div class="abs portrait" style="left:852px" role="img" aria-label="Portrait photo of team member Nadia Orsini"></div>

  <div class="abs member" style="left:93px">DARIO MENZEL</div>
  <div class="abs member" style="left:450px">PAOLO REYES</div>
  <div class="abs member" style="left:807px">NADIA ORSINI</div>
</section>

<section class="section reserve">
  <h2 class="abs heading center-x">Reserve Now</h2>
  <h3 class="abs heading center-x">EVERY GUEST IS SPECIAL HERE</h3>

  <div class="abs field" style="left:135px;top:260px">Name</div>
  <div class="abs field" style="left:475px;top:260px">Date</div>
  <div class="abs field" style="left:812px;top:260px">Person</div>
  <div class="abs field" style="left:135px;top:330px">E-Mail</div>
  <div class="abs field" style="left:475px;top:330px">Time</div>
  <div class="abs btn" style="left:812px;top:330px;width:253px;height:44px;line-height:44px">MAKE A Reservations</div>
</section>

<div class="abs events-head">
  <svg style="left:265px" width="40" height="34" viewBox="0 0 40 34"><ellipse cx="12" cy="18" rx="7" ry="13" fill="#2a0608"/><ellipse cx="28" cy="21" rx="7" ry="10" fill="#2a0608"/></svg>
  <svg style="left:625px" width="40" height="34" viewBox="0 0 40 34"><ellipse cx="12" cy="21" rx="7" ry="10" fill="#2a0608"/><ellipse cx="28" cy="18" rx="7" ry="13" fill="#2a0608"/></svg>
  <h2 class="abs heading center-x">Events</h2>
  <h3 class="abs heading center-x">JOIN US FOR SOMETHING SPECIAL</h3>
</div>

<section class="section events">
  <div class="abs burger" role="img" aria-label="Grilled burger with cheese, tomato and rocket"></div>

  <div class="abs point" style="top:138px"><span>All of your Lumera Café favorites are available, just right, easily and affordable.</span></div>
  <div class="abs point" style="top:240px"><span>Turn any large party or event into a Lumera Café celebration.</span></div>
  <div class="abs point" style="top:342px"><span>We will gladly honor requests to modify orders to suit specific health or dietary needs.</span></div>

  <div class="abs btn" style="left:906px;top:421px;width:159px;height:44px;line-height:44px">SEE ALL EVENTS</div>

  <p class="abs events-caption">Be it an intimate gathering of friends, a celebration of a corporate milestone, or an engagement reception, Lumera Café is the perfect venue. Reserve with us and let us be your host to a true event.</p>
  <span class="abs read-more" style="left:162px;top:548px">Read More</span>
</section>

<footer class="section footer">
  <h4 class="abs" style="left:162px;top:20px">Location</h4>
  <p class="abs" style="left:162px;top:80px;width:585px">Located in Harbour Point, Lumera Café has become a beacon for Service and Quality food. Enjoy an after-dinner coffee or drink from the spacious waterfront magical outdoors of the Marina or our comfortable indoor where you can relax and spend a memorable time with us.</p>
  <h4 class="abs" style="left:162px;top:216px">Social media</h4>
  <div class="abs" style="left:162px;top:290px;display:flex;gap:22px">
    <span class="social-dot"></span><span class="social-dot"></span><span class="social-dot"></span><span class="social-dot"></span><span class="social-dot"></span><span class="social-dot"></span>
  </div>

  <h4 class="abs" style="left:768px;top:20px">Contact us</h4>
  <div class="abs contact-field" style="top:83px">Name</div>
  <div class="abs contact-field" style="top:150px">Your Mail</div>
  <div class="abs contact-field" style="top:214px">Message</div>
  <div class="abs btn" style="left:768px;top:280px;width:149px;height:43px;line-height:43px;border-radius:3px">SUBMIT</div>
</footer>

<div class="section bottom-bar">© 2016 | ALL RIGHTS RESERVED</div>

</body>
</html>
```